Pecan Ridge Paving. Chip Seal Done Right

I need my card to have all my basic information on it. Keep it simple. Include web site, phone number and email address. Include phrase Chip Seal Done Right or Pecan Ridge’s Top Paving Company. Keep card simple. Include color and logo. Put all contact info on card. Make card simple and not complicated.

Here is infuriation yo out in business card

Dale R. Whitmore
830.555.0173 cell phone
Dalewhitmore7@mailbarn.net
www.pecanridgepaving.net

Target Market(s)

Hill Country Texas USA

Industry/Entity Type

Road chip seal

Contact Information for Business Card

We chip seal roads for ranches and property owners

Font styles to use
Serif
Sans Serif
Decorative
Script

Colors
0054AA
0677BA
7BADD7
CADEEF
E8F1F8
EB3D1F
EC4F4E
F09395
F8D3D4
FCEDEE

Requirements
Must have
• Keep it simply
Nice to have
• Logo and all basic info

```html
<!DOCTYPE html>
<html lang="en">
<head>
<meta charset="utf-8">
<title>Pecan Ridge Paving – Business Card</title>
<link rel="stylesheet" href="https://fonts.googleapis.com/css2?family=Montserrat:wght@400;500;600;800&family=Source+Sans+3:wght@400&display=swap">
<style>
  :root {
    --navy: #1d2456;
    --red: #b8212f;
    --paper: #ffffff;
    --page: #ffffff;
    --edge: #e3e3e3;
    --body-grey: #8a8a8a;
  }
  * { box-sizing: border-box; margin: 0; padding: 0; }
  html, body {
    width: 1200px; height: 1200px; overflow: hidden;
    background: var(--page);
    font-family: "Montserrat", sans-serif;
    color: var(--navy);
  }
  .canvas { position: relative; width: 1200px; height: 1200px; }

  .card {
    position: absolute;
    left: 319px; width: 555px; height: 317px;
    background: var(--paper);
    border: 1px solid var(--edge);
    box-shadow: 0 6px 18px rgba(0,0,0,0.12);
  }
  .card-front { top: 177px; }
  .card-back  { top: 532px; }

  .accent-bar {
    position: absolute; left: 0; top: 89px;
    width: 19px; height: 33px; background: var(--red);
  }
  .holder { position: absolute; left: 42px; top: 86px; }
  .holder-name {
    font-size: 20px; font-weight: 600; letter-spacing: 1px;
    color: var(--red); text-transform: uppercase; line-height: 1.2;
  }
  .holder-title {
    font-size: 16px; font-weight: 500; letter-spacing: 0.8px;
    color: var(--navy); text-transform: uppercase; margin-top: 2px;
  }

  .contact-list { position: absolute; left: 28px; top: 222px; list-style: none; }
  .contact-list li {
    display: flex; align-items: center; height: 20px;
    font-size: 15.5px; font-weight: 400; color: var(--navy);
  }
  .contact-list svg { width: 16px; height: 16px; margin-right: 18px; fill: var(--red); }

  /* wordmark */
  .wordmark { position: absolute; display: flex; align-items: center; }
  .wordmark-dot { background: var(--red); border-radius: 50%; flex: none; }
  .wordmark-text { flex: 1; display: flex; flex-direction: column; align-items: flex-end; }
  .wordmark-name {
    font-weight: 800; color: var(--navy); text-transform: uppercase;
    line-height: 1.05; text-align: right; white-space: nowrap;
  }
  .wordmark-tag {
    display: flex; align-items: center; white-space: nowrap;
    color: var(--red); font-weight: 500; letter-spacing: 0.6px;
  }
  .wordmark-tag::before { content: ""; display: block; height: 1px; background: var(--red); }

  .wordmark-small .wordmark-dot { width: 30px; height: 30px; margin-right: 10px; }
  .wordmark-small .wordmark-name { font-size: 21px; }
  .wordmark-small .wordmark-tag { font-size: 6.5px; margin-top: 4px; }
  .wordmark-small .wordmark-tag::before { width: 45px; margin-right: 5px; }

  .card-front .wordmark { left: 318px; top: 126px; width: 206px; height: 78px; }
  .card-back .wordmark  { left: 175px; top: 119px; width: 206px; height: 78px; }

  .card-url {
    position: absolute; left: 0; right: 0; top: 268px;
    text-align: center; font-size: 13.5px; letter-spacing: 0.5px; color: var(--navy);
  }

  .wordmark-large { left: 66px; top: 1009px; width: 360px; height: 138px; }
  .wordmark-large .wordmark-dot { width: 56px; height: 56px; margin-right: 18px; }
  .wordmark-large .wordmark-name { font-size: 38px; }
  .wordmark-large .wordmark-tag { font-size: 11.5px; margin-top: 8px; }
  .wordmark-large .wordmark-tag::before { width: 80px; margin-right: 8px; }

  .about-copy {
    position: absolute; left: 681px; top: 1004px; width: 438px;
    font-family: "Source Sans 3", sans-serif;
    font-size: 16.5px; line-height: 20.1px; color: var(--body-grey);
    text-align: justify; font-weight: 400; hyphens: auto;
  }
</style>
</head>
<body>
<main class="canvas">

  <section class="card card-front" aria-label="Business card front">
    <div class="accent-bar"></div>
    <div class="holder">
      <p class="holder-name">Dale R. Whitmore</p>
      <p class="holder-title">Chief Executive</p>
    </div>

    <div class="wordmark wordmark-small">
      <span class="wordmark-dot"></span>
      <div class="wordmark-text">
        <p class="wordmark-name">Pecan Ridge<br>Paving</p>
        <p class="wordmark-tag">CHIP SEAL DONE RIGHT</p>
      </div>
    </div>

    <ul class="contact-list">
      <li>
        <svg viewBox="0 0 24 24" aria-hidden="true"><path d="M6.6 10.8a15.1 15.1 0 0 0 6.6 6.6l2.2-2.2a1 1 0 0 1 1-.25 11.4 11.4 0 0 0 3.6.57 1 1 0 0 1 1 1V20a1 1 0 0 1-1 1A17 17 0 0 1 3 4a1 1 0 0 1 1-1h3.5a1 1 0 0 1 1 1c0 1.25.2 2.45.57 3.57a1 1 0 0 1-.25 1z"/></svg>
        830.555.0173
      </li>
      <li>
        <svg viewBox="0 0 24 24" aria-hidden="true"><path d="M2 5h20v14H2z M3.5 6.5 12 13l8.5-6.5v1.8L12 14.8 3.5 8.3z" fill-rule="evenodd"/></svg>
        Dalewhitmore7@mailbarn.net
      </li>
      <li>
        <svg viewBox="0 0 24 24" aria-hidden="true"><path d="M12 2a10 10 0 1 0 0 20 10 10 0 0 0 0-20zm-1 2.1V8H7.6A8 8 0 0 1 11 4.1zm2 0A8 8 0 0 1 16.4 8H13zM4.3 10H11v4H4.3a8 8 0 0 1 0-4zM13 10h6.7a8 8 0 0 1 0 4H13zm-5.4 6H11v3.9A8 8 0 0 1 7.6 16zm5.4 0h3.4a8 8 0 0 1-3.4 3.9z"/></svg>
        pecanridgepaving.net
      </li>
    </ul>
  </section>

  <section class="card card-back" aria-label="Business card back">
    <div class="wordmark wordmark-small">
      <span class="wordmark-dot"></span>
      <div class="wordmark-text">
        <p class="wordmark-name">Pecan Ridge<br>Paving</p>
        <p class="wordmark-tag">CHIP SEAL DONE RIGHT</p>
      </div>
    </div>
    <p class="card-url">www.pecanridgepaving.net</p>
  </section>

  <div class="wordmark wordmark-large">
    <span class="wordmark-dot"></span>
    <div class="wordmark-text">
      <p class="wordmark-name">Pecan Ridge<br>Paving</p>
      <p class="wordmark-tag">CHIP SEAL DONE RIGHT</p>
    </div>
  </div>

  <p class="about-copy">Lorem ipsum dolor sit amet, consectetur adipiscing elit, sed do eiusmod tempor incididunt ut labore et dolore magna aliqua. Quis ipsum suspendisse ultrices gravida. Risus commodo viverra maecenas accumsan lacus vel facilisis. Lorem ipsum dolor sit amet, consectetur adipiscing elit o eiusmod tempor incididunt ut labore et dolore magna aliqua. Quis ipsum suspendisse ultrices gravida. Risus commodo viverra maecenas accumsan lacus vel facilisis.</p>

</main>
</body>
</html>
```